Business Card Design Project

I am a psychotherapist, counselor and expressive arts therapist (means I use every art form imaginable in the service of healing). I'm just starting out in private practice in San Francisco, CA. I work with individual adults, children and families. I'd like the card to mirror the simplicity and color palate of my website. I also would love if there is a symbol, image of fire, flame or spark (that is warming, not frightening).

Check out my website: www.lorabecketmft.com

I want the cards to be printed in letter press so please keep that in mind!

Target Market(s)

Upper Middle Class Adults who are progressively minded, artistic or artists, open to psychotherapy, interested in health & healing.

Industry/Entity Type

Business

Requirements
Must have
• Text to be included:

Lora Becket
Counseling, Psychotherapy & Expressive Arts

2914 Alderwood Avenue, Suite D
San Francisco, CA 94127
p. 415.206.3791
lorajanebecket@meadowpost.net

www.lorabecketmft.com

MFT License Number 48671

It's OK to abbreviate Number to # or Street to St., etc.

Must be compatible with letter press printing.
Nice to have
• I don't have a logo. I don't expect designers to necessarily create one for me, but if someone comes up with a simple image (see above about flame), that would be great. I don't have much of a budget now, but expect that to change in the next year or so and then could buy a logo for my website, future letterhead, etc.

```html
<!DOCTYPE html>
<html lang="en">
<head>
<meta charset="utf-8">
<title>Lora Becket — Business Card</title>
<link rel="stylesheet" href="https://fonts.googleapis.com/css2?family=Tinos:ital,wght@0,700;1,700&display=swap">
<style>
  :root {
    --backdrop: #d9d2c3;
    --card-paper: #fbf1c8;
    --ink-red: #d9354f;
    --ink-grey: #55524c;
    --ornament-grey: #8a8478;
    --ornament-red: #d44a5f;
  }
  * { box-sizing: border-box; margin: 0; padding: 0; }
  html, body {
    width: 1200px;
    height: 902px;
    overflow: hidden;
  }
  body {
    background: var(--backdrop);
    position: relative;
    font-family: "Tinos", "Times New Roman", serif;
  }
  .business-card {
    position: absolute;
    left: 334px;
    width: 545px;
    height: 311px;
    background: var(--card-paper);
    box-shadow: 0 1px 3px rgba(0, 0, 0, 0.25);
    display: flex;
    flex-direction: column;
    align-items: center;
  }
  .business-card--neutral { top: 151px; }
  .business-card--warm { top: 485px; }

  .ornament {
    width: 270px;
    height: 46px;
    border-radius: 23px;
    opacity: 0.45;
  }
  .business-card--neutral .ornament { background: var(--ornament-grey); }
  .business-card--warm .ornament { background: var(--ornament-red); }
  .ornament--top { margin-top: 41px; }
  .ornament--bottom { margin-top: 11px; }

  .practitioner-name {
    margin-top: 8px;
    font-size: 39px;
    line-height: 40px;
    font-weight: 700;
    font-style: italic;
    text-transform: uppercase;
    letter-spacing: 0.5px;
    color: var(--ink-red);
  }
  .practice-tagline {
    font-size: 14.5px;
    line-height: 18px;
    font-weight: 700;
    font-style: italic;
    color: var(--ink-grey);
  }

  .contact-details {
    margin-top: 27px;
    text-align: center;
    font-size: 15.5px;
    line-height: 19.5px;
    font-weight: 700;
    color: var(--ink-grey);
  }
  .contact-details .web-name { color: var(--ink-red); }
</style>
</head>
<body>
  <section class="business-card business-card--neutral">
    <div class="ornament ornament--top" role="img" aria-label="Symmetrical scrollwork flourish in warm grey"></div>
    <h1 class="practitioner-name">Lora Becket</h1>
    <p class="practice-tagline">Counseling, Psychotherapy &amp; Expressive Arts</p>
    <div class="ornament ornament--bottom" role="img" aria-label="Symmetrical scrollwork flourish in warm grey"></div>
    <address class="contact-details">
      <span>2914 Alderwood Avenue, Suite D. San Francisco, CA 94127</span><br>
      <span>p. 415.206.3791 | lorajanebecket@meadowpost.net</span><br>
      <span>www.<span class="web-name">lorabecketmft</span>.com</span>
    </address>
  </section>

  <section class="business-card business-card--warm">
    <div class="ornament ornament--top" role="img" aria-label="Symmetrical scrollwork flourish in deep red"></div>
    <h1 class="practitioner-name">Lora Becket</h1>
    <p class="practice-tagline">Counseling, Psychotherapy &amp; Expressive Arts</p>
    <div class="ornament ornament--bottom" role="img" aria-label="Symmetrical scrollwork flourish in deep red"></div>
    <address class="contact-details">
      <span>2914 Alderwood Avenue, Suite D. San Francisco, CA 94127</span><br>
      <span>p. 415.206.3791 | lorajanebecket@meadowpost.net</span><br>
      <span>www.<span class="web-name">lorabecketmft</span>.com</span>
    </address>
  </section>
</body>
</html>
```